I.T Managed services requires company brochure.

We are want a design to show our clients what we are all about.

Information about our company and our services can be found on our website, www.zorvane.com.au

We want a corporate design but yet still fun and attractive.

I have also uploaded my LOGO, please incorporate it into the design.
Updates

Hi All

I am not 100% happy with the designs provided.   Please visit our web page
www.zorvane.com.au
We need the following
• - 4 page brochure of a4
• - the first page to have our logo on it with details from our phone number, web site address and info email address, at the back of it to have our 4 core services which are managed Services, Backup Solutions, Disaster Recovery Solutions and Remote Access management similar to our web site
• - the second page to have about us
• - the third page to have our services we offer and information
• - the fourth page to why us tab
• We want the brochure to be in 4 pages, to be back to front, no cartoon characters and to look professional and modern - to be similar matched to our web site.
can you please email me on malcolm@zorvane.com.au

Target Market(s)

Small to medium sized companies (1-200 employees)

Industry/Entity Type

It Company

Requirements
Must have
• Must elaborate on the 4 core product of ZRVN, which are

- Managed I.T Services
- Backup Management
- Disaster Recovery
- Remote Access

Also would like it to be in an A3 size format that folds into A4 by the slides folding in on either side.

Use the PDF example I uploaded as a guide for the look of the brochure.
Nice to have
• I have upload a brochure I found about solar power, I like the look of the brochure and want my brochure to be similar.

```html
<!DOCTYPE html>
<html lang="en">
<head>
<meta charset="utf-8">
<title>Zorvane Brochure – Outside Spread</title>
<link rel="stylesheet" href="https://fonts.googleapis.com/css2?family=Barlow+Condensed:wght@400;500&family=Roboto+Condensed:wght@300&display=swap">
<style>
  :root {
    --red: #d0202a;
    --red-deep: #b93a30;
    --salmon: #d9907c;
    --black: #0d0d0d;
    --grey-dark: #3c3c3c;
    --grey-mid: #6a6a6a;
    --grey-light: #9b9b9b;
    --panel: #2e2e2e;
    --panel-text: #d2d2d2;
    --rule: #c4c4c4;
    --white: #ffffff;
    --ink: #111111;
  }
  * { box-sizing: border-box; margin: 0; padding: 0; }
  html, body { width: 1200px; height: 849px; overflow: hidden; background: var(--white); }
  .spread {
    position: relative;
    width: 1200px;
    height: 849px;
    overflow: hidden;
    font-family: "Barlow Condensed", "Arial Narrow", sans-serif;
  }
  .spread__art { position: absolute; inset: 0; }

  .brand {
    position: absolute;
    left: 20px;
    top: 200px;
    display: flex;
    align-items: center;
    gap: 10px;
  }
  .brand__dot {
    width: 30px; height: 30px;
    border-radius: 50%;
    background: var(--red);
  }
  .brand__name {
    font-size: 40px;
    font-weight: 500;
    letter-spacing: 3px;
    color: var(--ink);
    line-height: 1;
  }

  .cover-title {
    position: absolute;
    left: 70px;
    width: 316px;
    top: 412px;
    text-align: center;
    line-height: 1;
  }
  .cover-title__top { display: block; font-size: 62px; font-weight: 500; color: var(--red); }
  .cover-title__bottom { display: block; margin-top: 22px; font-size: 54px; font-weight: 400; color: var(--ink); }

  .flap-title {
    position: absolute;
    left: 805px;
    width: 300px;
    top: 478px;
    text-align: center;
    font-size: 68px;
    font-weight: 400;
    line-height: 1;
    color: var(--red);
  }

  .about {
    position: absolute;
    left: 390px;
    top: 0;
    width: 415px;
    padding: 26px 24px 0 24px;
    color: var(--panel-text);
    font-family: "Roboto Condensed", "Arial Narrow", sans-serif;
    font-size: 15.4px;
    font-weight: 300;
    line-height: 20px;
    hyphens: auto;
  }
  .about__heading {
    font-family: "Barlow Condensed", "Arial Narrow", sans-serif;
    font-size: 40px;
    font-weight: 400;
    color: var(--red);
    line-height: 1;
    margin: 0 0 14px 3px;
  }
  .about p { margin-bottom: 13px; }
  .about__lead {
    border-left: 5px solid var(--rule);
    padding-left: 9px;
  }
</style>
</head>
<body>
<main class="spread">
  <svg class="spread__art" viewBox="0 0 1200 849" width="1200" height="849" aria-hidden="true">
    <!-- left cover panel -->
    <rect x="0" y="0" width="390" height="849" fill="var(--grey-mid)"/>
    <polygon points="0,0 390,0 390,300 0,300" fill="var(--salmon)"/>
    <polygon points="70,0 170,0 390,150 390,250" fill="var(--red-deep)"/>
    <polygon points="230,285 300,250 390,300 320,320" fill="var(--black)"/>
    <polygon points="0,400 390,230 390,320 0,480" fill="var(--grey-dark)"/>
    <polygon points="0,480 390,320 390,420 0,560" fill="var(--grey-light)"/>
    <polygon points="0,575 110,640 0,700" fill="var(--black)"/>
    <polygon points="0,720 230,600 390,690 390,760 150,849 0,849" fill="var(--red-deep)"/>
    <polygon points="150,849 390,720 390,849" fill="var(--salmon)"/>
    <polygon points="0,780 120,849 0,849" fill="var(--grey-dark)"/>
    <!-- right flap panel -->
    <rect x="805" y="0" width="395" height="849" fill="var(--grey-mid)"/>
    <polygon points="805,0 1200,0 1200,260 805,260" fill="var(--salmon)"/>
    <polygon points="815,200 1200,30 1200,410" fill="var(--red)"/>
    <polygon points="1100,0 1200,0 1200,40" fill="var(--black)"/>
    <polygon points="880,250 940,250 960,300 905,300" fill="var(--black)"/>
    <polygon points="805,300 1200,330 1200,470 805,400" fill="var(--grey-dark)"/>
    <polygon points="805,560 1200,430 1200,600 805,720" fill="var(--grey-light)"/>
    <polygon points="805,720 1200,590 1200,700 1020,849 805,849" fill="var(--salmon)"/>
    <polygon points="960,730 1200,640 1200,849 1090,849" fill="var(--red-deep)"/>
    <polygon points="1150,600 1200,580 1200,700" fill="var(--black)"/>
    <!-- white pointers -->
    <polygon points="0,15 384,200 0,410" fill="var(--white)"/>
    <polygon points="390,305 34,517 390,730" fill="var(--white)"/>
    <polygon points="805,305 1160,517 805,730" fill="var(--white)"/>
    <!-- centre about panel -->
    <rect x="390" y="0" width="415" height="849" fill="var(--panel)"/>
    <polygon points="390,100 805,330 805,520 390,290" fill="#ffffff" opacity="0.05"/>
    <polygon points="390,560 805,330 805,470 390,720" fill="#ffffff" opacity="0.06"/>
  </svg>

  <div class="brand">
    <span class="brand__dot"></span>
    <span class="brand__name">ZORVANE</span>
  </div>

  <h1 class="cover-title">
    <span class="cover-title__top">ZRVN</span>
    <span class="cover-title__bottom">ZORVANE</span>
  </h1>

  <div class="flap-title">BROCHURE</div>

  <section class="about">
    <h2 class="about__heading">ABOUT US</h2>
    <p class="about__lead">Zorvane is a Boutique I.T. Services provider which caters for the individual needs and requirements for small to medium entities (SME's). Zorvane was founded in 2010 and aims at providing Enterprise solutions at cost effective needs to our clients.</p>
    <p>We aim in delivering excellence and ensuring we provide high end support for your business needs 24/7. Our goals are to deliver real business process improvements and contribute to customer values and needs. The utmost priority is provided to our valued customers in implementing systems that provide an efficient value driven IT solution for any situation.</p>
    <p>We connect an SME with cost effective, valuable and high end technology partner to deliver our services to our customers. Our staff and engineers have a minimum of 10 years work experience in small, medium and enterprise support and are at your disposal 24 hours, 7 days a week.</p>
    <p>Zorvane provides cloud solutions to a diverse client base ensuring in allowing our clients to meet some of their toughest business challenges they may face. Our Primary aims is to understand your business needs and provide you the best solution that will meet your requirements for your business.</p>
    <p>Zorvane operates out of Melbourne CBD, but will service Melbourne's Northern, Southern, Eastern and Western suburbs (including rural Victoria). Zorvane also branches out to other states in Australia and provides support to various businesses in South Australia, Brisbane and Tasmania.</p>
    <p>Zorvane is proud to be a 100% Australian owned and operated company, which endeavours to support the Australia Economy.</p>
    <p>Become part of the family at Zorvane!!!</p>
  </section>
</main>
</body>
</html>
```